Creative Brief
Buisness Card Larkfield Homes
Card for Larkfield
Professional
Cal Dorsey
Constrution Supervisor
Larkfield Homes
PO Box 530618
Houston, Texas 77064
cdorsey@larkfield-homes.example
www.larkfield-homes.example
Logo file

```html
<!DOCTYPE html>
<html lang="en">
<head>
<meta charset="utf-8">
<title>Larkfield Homes — Stationery</title>
<link href="https://fonts.googleapis.com/css2?family=Open+Sans:wght@400;600;700&display=swap" rel="stylesheet">
<style>
  :root {
    --backdrop: #3b3b3d;
    --paper: #ffffff;
    --ink: #1a1a1a;
    --gold-dark: #7a5410;
    --gold: #c8921e;
    --gold-light: #e8b84a;
    --black: #0c0c0c;
  }
  * { box-sizing: border-box; margin: 0; padding: 0; }
  html, body { width: 1200px; height: 921px; overflow: hidden; }
  body {
    position: relative;
    background: var(--backdrop);
    font-family: "Open Sans", Arial, sans-serif;
    color: var(--ink);
  }
  .sheet { position: absolute; background: var(--paper); box-shadow: 0 4px 14px rgba(0,0,0,.45); }
  .gold-band {
    position: absolute; left: 0; right: 0;
    background: linear-gradient(90deg, var(--gold-dark) 0%, var(--gold) 35%, var(--gold-light) 60%, var(--gold) 80%, var(--gold-dark) 100%);
  }
  .brand { position: absolute; display: flex; align-items: center; gap: 6px; background: var(--black); padding: 6px 8px; }
  .brand-square { width: 14px; height: 14px; background: var(--gold); flex: none; }
  .brand-name { color: var(--gold-light); font-weight: 600; font-size: 11px; letter-spacing: .5px; white-space: nowrap; }
  .web { position: absolute; left: 0; right: 0; text-align: center; font-size: 9px; font-weight: 600; color: var(--ink); }
  .web span { color: var(--gold); }

  /* Letterhead */
  .letterhead { left: 75px; top: 125px; width: 486px; height: 686px; }
  .letterhead .gold-band { top: 14px; height: 62px; }
  .letterhead .brand { left: 14px; top: 20px; }
  .letterhead .contact { position: absolute; right: 16px; top: 19px; font-size: 6.5px; line-height: 8.2px; color: #fff; font-style: normal; }
  .letterhead .web { bottom: 14px; }

  /* Business cards */
  .card { position: absolute; top: 105px; width: 212px; height: 132px; background: var(--black); border-radius: 6px; box-shadow: 0 4px 12px rgba(0,0,0,.5); overflow: hidden; }
  .card-front { left: 631px; }
  .card-front .brand { left: 50%; top: 34px; transform: translateX(-50%); border: 1px solid var(--gold); }
  .card-front .web { bottom: 12px; color: #fff; }
  .card-back { left: 866px; }
  .card-back .brand { left: 10px; top: 12px; width: 70px; padding: 6px 4px; flex-direction: column; gap: 4px; border: 1px solid var(--gold); }
  .card-back .brand-square { width: 18px; height: 18px; }
  .card-back .brand-name { font-size: 7px; letter-spacing: .2px; }
  .card-back .person { position: absolute; left: 92px; top: 12px; }
  .card-back .person-name { font-size: 12px; font-weight: 700; color: var(--gold-light); }
  .card-back .person-role { font-size: 6.5px; color: #ccc; }
  .card-back .details { position: absolute; left: 92px; top: 50px; font-size: 6px; line-height: 8.5px; color: #ddd; }
  .card-back .gold-band { bottom: 16px; height: 6px; }
  .card-back .web { bottom: 4px; color: #fff; font-size: 6.5px; }

  /* Envelope */
  .envelope { left: 591px; top: 324px; width: 487px; height: 237px; }
  .envelope .gold-band { top: 0; height: 50px; }
  .envelope .flap { position: absolute; left: 0; top: 50px; width: 100%; height: 18px; }
  .envelope .brand { left: 50%; top: 8px; transform: translateX(-50%); }

  /* Compliment slip */
  .slip { left: 591px; top: 599px; width: 487px; height: 212px; }
  .slip .gold-band { top: 12px; height: 52px; }
  .slip .brand { left: 12px; top: 18px; }
  .slip .address { position: absolute; left: 150px; top: 48px; font-size: 6.5px; color: #fff; }
  .slip .web { bottom: 12px; }
</style>
</head>
<body>

<section class="sheet letterhead">
  <div class="gold-band"></div>
  <div class="brand"><span class="brand-square"></span><span class="brand-name">Larkfield Homes</span></div>
  <address class="contact">
    Larkfield Homes<br>PO Box 530618<br>Houston, Texas 77064<br>
    tel (281) 555-0142<br>fax (281) 555-0179<br>cdorsey@larkfield-homes.example
  </address>
  <p class="web"><span>www.</span>larkfield-homes<span>.example</span></p>
</section>

<section class="card card-front">
  <div class="brand"><span class="brand-square"></span><span class="brand-name">Larkfield Homes</span></div>
  <p class="web">www.larkfield-homes.example</p>
</section>

<section class="card card-back">
  <div class="brand"><span class="brand-square"></span><span class="brand-name">Larkfield Homes</span></div>
  <div class="person">
    <p class="person-name">Cal Dorsey</p>
    <p class="person-role">Construction Supervisor</p>
  </div>
  <p class="details">
    Larkfield Homes<br>PO Box 530618<br>Houston, Texas 77064<br>
    tel (281) 555-0142<br>cdorsey@larkfield-homes.example
  </p>
  <div class="gold-band"></div>
  <p class="web">www.larkfield-homes.example</p>
</section>

<section class="sheet envelope">
  <div class="gold-band"></div>
  <svg class="flap" viewBox="0 0 487 18" preserveAspectRatio="none">
    <polygon points="0,0 487,0 470,18 17,18" fill="#a87418"/>
  </svg>
  <div class="brand"><span class="brand-square"></span><span class="brand-name">Larkfield Homes</span></div>
</section>

<section class="sheet slip">
  <div class="gold-band"></div>
  <div class="brand"><span class="brand-square"></span><span class="brand-name">Larkfield Homes</span></div>
  <p class="address">Larkfield Homes · PO Box 530618 · Houston, Texas 77064</p>
  <p class="web"><span>www.</span>larkfield-homes<span>.example</span></p>
</section>

</body>
</html>
```